The Brightwell Clinic :

At The Brightwell Clinic our goal is to provide the most skilled and advanced examination and treatment of the upper neck for superior long-term outcomes for those experiencing headache or migraine.

If a spinal disorder is responsible for the headache and migraine condition the disorder will involve one or more of the top three spinal segments. The fundamental and most powerful feature of The Brightwell Clinic is our method of examining the movements of the top three spinal segments.

We would like the design should communicate professionalism and specialisation.
Updates

Don't necessarily have to have the photos provided.Photo was used for promotional material. I dont have a logo as yet what I  would also like designed.

Project Deadline Extended
Reason: Opening has been delayed due to construction issues of building.

Industry/Entity Type

Clinic

Contact Information for Business Card

The Brightwell Clinic
Suite 3, Oakvale Heath Centre
87 Ferncliff Drive, Harbourview NSW 2417
Tel : 63 71 2946 www.thebrightwellclinic.com.au

Requirements
Must have
• Mr Carl Pettigrew
Senior Physiotherapist / Senior Accredited Exercise Physiologist
B. Hlth. Sc. (Physiotherapy), B. Mv. Sc. (Clinical Exercise), Dip. M.T, MPAA, MCEPA, MSPA, MRCSM.

Appointment area on back of card

```html
<!DOCTYPE html>
<html lang="en">
<head>
<meta charset="utf-8">
<title>The Brightwell Clinic – Business Card</title>
<link rel="stylesheet" href="https://fonts.googleapis.com/css2?family=Exo+2:wght@500;600;700&family=Oswald:wght@300&family=Questrial&family=Dosis:wght@200;300&display=swap">
<style>
  :root {
    --purple: #8e3d96;
    --purple-light: #a869ae;
    --lilac: #dcc1e0;
    --red: #e3141c;
    --ink: #2a2a2a;
    --white: #ffffff;
  }
  * { margin: 0; padding: 0; box-sizing: border-box; }
  html, body { width: 1039px; height: 1200px; overflow: hidden; background: var(--white); }
  .stage {
    position: absolute; left: 0; top: 0;
    width: 1280px; height: 1470px;
    transform: scale(0.81172); transform-origin: 0 0;
  }
  .card { position: absolute; overflow: hidden; }

  /* Front */
  .card--front { left: 104px; top: 58px; width: 1063px; height: 614px; background: var(--purple); }
  .front-art { position: absolute; inset: 0; }
  .slogan-word {
    position: absolute; left: 92px; top: 70px;
    font-family: "Dosis", sans-serif; font-weight: 200; font-size: 92px; line-height: 100px;
    color: rgba(220, 190, 226, 0.4); letter-spacing: 4px;
  }
  .slogan-label {
    position: absolute; left: 66px; top: 179px; width: 502px; height: 50px;
    background: linear-gradient(90deg, rgba(255,255,255,0) 0%, rgba(255,255,255,0.55) 35%, var(--white) 70%);
    font-family: "Dosis", sans-serif; font-weight: 300; font-size: 42px;
    line-height: 50px; color: var(--purple-light); padding-left: 40px; white-space: nowrap;
  }
  .clinic-name {
    position: absolute; left: 52px; top: 382px;
    font-family: "Exo 2", sans-serif; font-weight: 600; font-size: 46px; color: var(--white);
  }
  .practitioner {
    position: absolute; right: 406px; top: 438px; height: 50px; padding: 0 0 0 20px;
    background: linear-gradient(90deg, rgba(255,255,255,0.28), rgba(255,255,255,0.12) 80%, rgba(255,255,255,0));
    font-size: 37px; line-height: 52px; color: var(--white); white-space: nowrap;
  }
  .practitioner__title { font-family: "Oswald", sans-serif; font-weight: 300; }
  .practitioner__name { font-family: "Exo 2", sans-serif; font-weight: 700; }
  .role {
    position: absolute; right: 406px; top: 488px;
    font-family: "Oswald", sans-serif; font-weight: 300; font-size: 26px; letter-spacing: 0.5px;
    color: var(--white); white-space: nowrap;
  }
  .credentials {
    position: absolute; right: 406px; top: 532px; text-align: right; white-space: nowrap;
    font-family: "Oswald", sans-serif; font-weight: 300; font-size: 19px; letter-spacing: 0.5px;
    line-height: 26px; color: var(--white);
  }

  /* Back */
  .card--back { left: 102px; top: 769px; width: 1066px; height: 618px; border: 3px solid #000; background: var(--white); }
  .back-header {
    position: absolute; left: 0; top: 0; width: 100%; height: 211px;
    background: linear-gradient(90deg, var(--lilac) 0%, #f3e9f4 40%, var(--white) 70%);
  }
  .header-photo { position: absolute; right: 24px; top: 0; width: 264px; height: 211px; }
  .back-clinic {
    position: absolute; left: 44px; top: 40px;
    font-family: "Exo 2", sans-serif; font-weight: 600; font-size: 35px; color: var(--ink);
  }
  .address {
    position: absolute; left: 44px; top: 84px;
    font-family: "Questrial", sans-serif; font-size: 27px; line-height: 33px; letter-spacing: 1px; color: var(--ink);
  }
  .contact {
    position: absolute; left: 44px; top: 154px; white-space: nowrap;
    font-family: "Exo 2", sans-serif; font-weight: 700; color: var(--ink);
  }
  .contact__tel { font-size: 31px; }
  .contact__web { font-size: 26px; color: var(--purple); letter-spacing: 1px; margin-left: 6px; }
  .appointments { position: absolute; left: 0; top: 211px; width: 100%; height: 346px; }
  .appointments__head {
    height: 42px; background: var(--purple); display: flex;
    font-family: "Questrial", sans-serif; font-size: 22px; letter-spacing: 4px; color: var(--white); line-height: 46px;
  }
  .appointments__head span { width: 50%; padding-left: 45px; }
  .appointments__head span + span { padding-left: 30px; }
  .appointments__grid { position: absolute; left: 0; top: 42px; width: 100%; height: 304px; }
  .back-footer {
    position: absolute; left: 0; bottom: 0; width: 100%; height: 58px;
    background: linear-gradient(180deg, var(--purple) 0%, #c79dcc 55%, var(--white) 100%);
    text-align: center; font-family: "Exo 2", sans-serif; font-weight: 600; font-size: 23px;
    letter-spacing: 4px; color: var(--white); line-height: 38px;
  }
</style>
</head>
<body>
<div class="stage">

  <section class="card card--front">
    <svg class="front-art" width="1063" height="614" viewBox="0 0 1063 614">
      <defs>
        <radialGradient id="portrait-tone" cx="0.6" cy="0.45" r="0.6">
          <stop offset="0" stop-color="#f4e6dc"/>
          <stop offset="0.6" stop-color="#eddcc6"/>
          <stop offset="1" stop-color="#d9c39e"/>
        </radialGradient>
      </defs>
      <circle cx="822" cy="262" r="228" fill="#a35aab"/>
      <circle cx="829" cy="265" r="217" fill="url(#portrait-tone)" role="img" aria-label="Portrait photo of a smiling woman"/>
      <polyline points="91,205 59,205 59,378" fill="none" stroke="var(--red)" stroke-width="3"/>
      <line x1="567" y1="205" x2="738" y2="205" stroke="var(--red)" stroke-width="3"/>
      <circle cx="762" cy="205" r="26" fill="none" stroke="var(--red)" stroke-width="3"/>
      <circle cx="762" cy="205" r="17" fill="var(--red)"/>
    </svg>
    <div class="slogan-word">restore</div>
    <div class="slogan-label">clarity from the top down</div>
    <h1 class="clinic-name">The Brightwell Clinic</h1>
    <div class="practitioner"><span class="practitioner__title">Mr </span><span class="practitioner__name">Carl Pettigrew</span></div>
    <div class="role">Senior Physiotherapist / Senior Accredited Exercise Physiologist</div>
    <div class="credentials">B. Hlth. Sc. (Physiotherapy), B. Mv. Sc. (Clinical Exercise),<br>Dip. M.T, MPAA, MCEPA, MSPA, MRCSM.</div>
  </section>

  <section class="card card--back">
    <div class="back-header"></div>
    <svg class="header-photo" width="264" height="211" viewBox="0 0 264 211" role="img" aria-label="Photo of a woman holding her temples with a headache">
      <defs>
        <linearGradient id="header-photo-tone" x1="0" y1="0" x2="1" y2="0">
          <stop offset="0" stop-color="#ffffff" stop-opacity="0"/>
          <stop offset="0.3" stop-color="#dcdcdc"/>
          <stop offset="0.7" stop-color="#cfcfcf"/>
          <stop offset="1" stop-color="#ececec"/>
        </linearGradient>
      </defs>
      <rect width="264" height="211" fill="url(#header-photo-tone)"/>
    </svg>
    <h2 class="back-clinic">The Brightwell Clinic</h2>
    <p class="address">Suite 3, Oakvale Heath Centre<br>87 Ferncliff Drive, Harbourview NSW 2417</p>
    <p class="contact"><span class="contact__tel">Tel : 63 71 2946</span> <span class="contact__web">www.thebrightwellclinic.com.au</span></p>

    <div class="appointments">
      <div class="appointments__head"><span>DATE / TIME</span><span>DATE / TIME</span></div>
      <svg class="appointments__grid" width="1060" height="304" viewBox="0 0 1060 304">
        <g stroke="var(--purple-light)" stroke-width="1.5">
          <line x1="530" y1="0" x2="530" y2="304"/>
          <line x1="0" y1="57" x2="1060" y2="57"/>
          <line x1="0" y1="119" x2="1060" y2="119"/>
          <line x1="0" y1="180" x2="1060" y2="180"/>
          <line x1="0" y1="242" x2="1060" y2="242"/>
        </g>
      </svg>
    </div>
    <div class="back-footer">restore clarity from the top down</div>
  </section>

</div>
</body>
</html>
```